broucher for electrical contracting buisness

use website template and attached files for colour scheme / ideas

Industry/Entity Type

Electrical

Requirements
Must have
• A5 folded to A4 4 pp format
• use the written content in the broucher word document as a guide

```html
<!DOCTYPE html>
<html lang="en">
<head>
<meta charset="utf-8">
<title>Brayford Electrical – Folded Brochure</title>
<link rel="stylesheet" href="https://fonts.googleapis.com/css2?family=Montserrat:wght@500;600;700;800&family=Open+Sans:wght@400;600;700&family=Roboto+Condensed:wght@400;700&display=swap">
<style>
  :root {
    --navy: #1d3378;
    --red: #d0202a;
    --paper: #f4f5f8;
    --ink: #24305e;
    --backdrop: #3a3a3c;
    --photo-a: #b9b6ae;
    --photo-b: #6f6f72;
    --interior-a: #c9ccd2;
    --interior-b: #6e7179;
  }
  * { box-sizing: border-box; margin: 0; padding: 0; }
  html, body { width: 1200px; height: 789px; overflow: hidden; }
  body { background: var(--backdrop); font-family: "Open Sans", sans-serif; color: var(--ink); }

  .spread { position: absolute; left: 77px; top: 24px; width: 1046px; height: 740px; display: flex; box-shadow: 0 10px 30px rgba(0,0,0,.45); }
  .page { position: relative; width: 523px; height: 740px; background: var(--paper); overflow: hidden; }
  .page--back { border-right: 1px solid #d8dae0; }

  .shape-layer { position: absolute; inset: 0; width: 523px; height: 740px; }

  /* back page */
  .intro { position: absolute; left: 40px; top: 46px; width: 300px; font-size: 10px; line-height: 1.45; color: var(--ink); }
  .intro p + p { margin-top: 10px; }
  .interior-photo { position: absolute; left: 40px; top: 200px; width: 483px; height: 250px; background: linear-gradient(160deg, var(--interior-a), var(--interior-b)); }

  .contact { position: absolute; left: 40px; top: 478px; width: 360px; }
  .contact__rule { width: 220px; height: 1px; background: var(--ink); margin-bottom: 8px; }
  .contact__title { font-family: "Montserrat", sans-serif; font-weight: 700; font-size: 15px; color: var(--red); margin-bottom: 10px; }
  .contact__item { display: flex; align-items: flex-start; gap: 8px; font-size: 11px; line-height: 1.4; margin-bottom: 5px; }
  .contact__item svg { flex: 0 0 10px; margin-top: 3px; }

  .brand { font-family: "Montserrat", sans-serif; font-weight: 800; color: var(--navy); letter-spacing: .5px; line-height: 1; }
  .brand--back { position: absolute; right: 36px; top: 560px; font-size: 20px; }
  .social { position: absolute; right: 36px; top: 655px; display: flex; gap: 8px; }
  .social span { width: 18px; height: 18px; border-radius: 50%; background: var(--paper); display: block; }
  .website { position: absolute; left: 40px; top: 705px; display: flex; align-items: center; gap: 8px; color: #fff; font-size: 14px; font-weight: 600; }

  /* front page */
  .brand--front { position: absolute; right: 36px; top: 38px; font-size: 30px; }
  .brand__sub { position: absolute; right: 36px; top: 74px; font-family: "Montserrat", sans-serif; font-weight: 600; font-size: 10px; letter-spacing: 2px; color: var(--navy); }
  .panel-photo { position: absolute; left: 0; top: 118px; width: 523px; height: 400px; background: linear-gradient(135deg, var(--photo-a), var(--photo-b)); clip-path: polygon(0 5%, 100% 0, 100% 78%, 0 100%); }

  .tagline { position: absolute; left: 40px; top: 548px; font-family: "Roboto Condensed", sans-serif; text-transform: uppercase; line-height: 1.15; }
  .tagline__lead { font-weight: 700; font-size: 28px; color: var(--red); }
  .tagline__line { font-size: 16px; color: var(--navy); }
  .tagline__accent { font-weight: 700; font-size: 12px; color: var(--red); }
  .tagline__close { font-weight: 700; font-size: 16px; color: var(--navy); }

  .emergency { position: absolute; right: 30px; top: 528px; width: 130px; text-align: left; font-family: "Roboto Condensed", sans-serif; }
  .emergency__ring { position: absolute; right: 4px; top: 0; width: 48px; height: 48px; border: 3px solid var(--red); border-radius: 50%; }
  .emergency__hours { font-weight: 700; font-size: 38px; color: var(--navy); line-height: 1; }
  .emergency__label { font-weight: 700; font-size: 15px; color: var(--navy); line-height: 1; }
  .emergency__label em { font-style: normal; color: var(--red); font-size: 13px; }

  .call { position: absolute; left: 40px; top: 700px; color: #fff; font-family: "Montserrat", sans-serif; font-weight: 700; font-size: 14px; }
  .abn { position: absolute; right: 24px; top: 666px; color: #fff; font-family: "Montserrat", sans-serif; font-weight: 600; font-size: 13px; }
</style>
</head>
<body>
<main class="spread">

  <!-- back cover -->
  <section class="page page--back">
    <div class="intro">
      <p>Providing you with high quality electrical componentry and proven industry know how, at Brayford Electrical you can rest assured your job will be completed to standard and on time. We pride ourselves on providing you with professional electrical services at competitive prices.</p>
      <p>With a qualified workforce, fleet of specialist vehicles, modern plant and equipment, Brayford Electrical provides cost efficient and innovative electrical solutions to a wide range of clients and industries.</p>
    </div>

    <div class="interior-photo" role="img" aria-label="Photo of a modern lit reception interior with ceiling downlights"></div>

    <div class="contact">
      <div class="contact__rule"></div>
      <h2 class="contact__title">CONTACT DETAILS</h2>
      <div class="contact__item">
        <svg width="10" height="12" viewBox="0 0 10 12"><path d="M5 0a4 4 0 0 0-4 4c0 3 4 8 4 8s4-5 4-8a4 4 0 0 0-4-4zm0 5.5A1.5 1.5 0 1 1 5 2.5a1.5 1.5 0 0 1 0 3z" fill="var(--red)"/></svg>
        <span>Address line 1, Address line 1<br>Address line 2, Address line 2, Address line 2</span>
      </div>
      <div class="contact__item">
        <svg width="10" height="10" viewBox="0 0 10 10"><path d="M2 0l2 2.5-1.2 1.3a6 6 0 0 0 3.4 3.4L7.5 6 10 8 8.5 10C4 10 0 6 0 1.5z" fill="var(--red)"/></svg>
        <span>0123 555 010</span>
      </div>
      <div class="contact__item">
        <svg width="10" height="10" viewBox="0 0 10 10"><rect x="2" y="0" width="6" height="3" fill="var(--red)"/><rect x="0" y="3.5" width="10" height="4" fill="var(--red)"/><rect x="2" y="7" width="6" height="3" fill="var(--red)"/></svg>
        <span>0123 555 010</span>
      </div>
      <div class="contact__item">
        <svg width="10" height="8" viewBox="0 0 10 8"><rect x=".5" y=".5" width="9" height="7" fill="none" stroke="var(--red)"/><path d="M.5 .5 5 4.5 9.5 .5" fill="none" stroke="var(--red)"/></svg>
        <span>info@brayfordelectrical.com</span>
      </div>
    </div>

    <div class="brand brand--back">BRAYFORD ELECTRICAL</div>

    <svg class="shape-layer" viewBox="0 0 523 740" aria-hidden="true">
      <polygon points="330,690 380,640 523,640 523,690" fill="var(--navy)"/>
      <polygon points="0,690 523,690 523,740 0,740" fill="var(--red)"/>
    </svg>

    <div class="social" aria-label="Social links"><span></span><span></span><span></span></div>

    <div class="website">
      <svg width="14" height="14" viewBox="0 0 14 14"><circle cx="7" cy="7" r="6" fill="none" stroke="#fff" stroke-width="1.3"/><ellipse cx="7" cy="7" rx="2.6" ry="6" fill="none" stroke="#fff" stroke-width="1.1"/><line x1="1" y1="7" x2="13" y2="7" stroke="#fff" stroke-width="1.1"/></svg>
      <span>www.brayfordelectrical.com</span>
    </div>
  </section>

  <!-- front cover -->
  <section class="page page--front">
    <div class="brand brand--front">BRAYFORD ELECTRICAL</div>
    <div class="brand__sub">EC 00000</div>

    <svg class="shape-layer" viewBox="0 0 523 740" aria-hidden="true">
      <polygon points="0,110 190,98 200,112 0,128" fill="var(--red)"/>
    </svg>

    <div class="panel-photo" role="img" aria-label="Photo of a gloved electrician testing a switchboard with a multimeter"></div>

    <svg class="shape-layer" viewBox="0 0 523 740" aria-hidden="true">
      <polygon points="220,520 523,430 523,452 240,530" fill="var(--red)"/>
      <polygon points="0,690 330,650 330,740 0,740" fill="var(--navy)"/>
      <polygon points="320,652 523,624 523,740 320,740" fill="var(--red)"/>
    </svg>

    <div class="tagline">
      <div class="tagline__lead">We Pride</div>
      <div class="tagline__line">Ourselves on providing you</div>
      <div class="tagline__accent">With professional electrical services</div>
      <div class="tagline__close">At competitive prices</div>
    </div>

    <div class="emergency">
      <span class="emergency__ring"></span>
      <div class="emergency__hours">24/7</div>
      <div class="emergency__label">Emergency<br><em>Services</em></div>
    </div>

    <div class="call">CALL US NOW - 123 555 0190</div>
    <div class="abn">ABN: 12 3456 789 00</div>
  </section>

</main>
</body>
</html>
```